Sam Greenfield Billboard

**Task Description: Billboard Design for Self Storage Facility**

**Objective:**
Design a captivating billboard to promote our self-storage facility with a focus on our convenient location and online rental capabilities.

**Key Messages to Include:**
1. **Location Emphasis:** Highlight that our facility is located right beside the billboard (maybe by using an arrow pointing left).
2. **Online Rental Convenience:** Feature prominently that customers can "Rent Online Anytime!” or that we are "Always Open Online!"

**Target Audience:**
- Local residents looking for convenient self-storage solutions.
- Businesses needing storage space accessible around the clock.

**Design Elements:**
1. **Visual Impact:** Eye-catching graphics and colors that stand out against the surroundings.
2. **Clear Text:** Bold and concise messaging that can be read and understood quickly.
3. **Contact Information:** Include our phone number and website URL for easy access to further information.

**Additional Information:**
- Billboard dimensions: 12 ft. x 24 ft.
- Preferred color scheme: Bright and attention-grabbing, but professional.
- Branding: Incorporate our logo and brand colors to maintain consistency.

**Deliverables:**
- High-resolution digital file compatible with billboard printing specifications.
- Consider mockups or visualizations for presentation purposes.

Please note that I have attached current logos/graphics that we would love to incorporate into the billboard as well as a picture of our current billboard. Our logo (Sam Greenfield Self Storage - SG navy.png) MUST be incorporated into the billboard. Also feel free to add any of the current descriptions from the picture of our current billboard into the design. Instead of using "Climate Controlled" use "Temperature Controlled". Thank you for your attention to these details. We look forward to reviewing your proposed design!

```html
<!DOCTYPE html>
<html lang="en">
<head>
<meta charset="utf-8">
<title>Sam Greenfield Self Storage Billboard</title>
<link href="https://fonts.googleapis.com/css2?family=Montserrat:wght@400;500;600;800;900&display=swap" rel="stylesheet">
<style>
  :root {
    --navy: #2b2a73;
    --gold: #8e7352;
    --white: #ffffff;
    --paper: #f6f6f8;
  }
  * { margin: 0; padding: 0; box-sizing: border-box; }
  html, body { width: 1200px; height: 785px; overflow: hidden; background: var(--white); }
  .billboard {
    position: relative; width: 1200px; height: 785px; overflow: hidden;
    background: var(--white);
    font-family: "Montserrat", Arial, sans-serif;
  }
  .backdrop { position: absolute; inset: 0; }
  .brand {
    position: absolute; left: 34px; top: 34px;
    padding: 10px 18px 8px;
    border: 3px solid var(--gold);
    color: var(--navy);
  }
  .brand-name { font-weight: 800; font-size: 34px; letter-spacing: 0.5px; line-height: 1; white-space: nowrap; }
  .brand-sub { font-weight: 800; font-size: 15px; letter-spacing: 11px; line-height: 1; margin-top: 6px; white-space: nowrap; }
  .headline { position: absolute; left: 30px; top: 150px; font-weight: 900; line-height: 0.9; white-space: nowrap; }
  .headline-top { color: var(--navy); font-size: 90px; letter-spacing: -1px; }
  .headline-bottom { color: var(--gold); font-size: 132px; letter-spacing: -2px; }
  .features {
    position: absolute; left: 30px; top: 404px; width: 720px; height: 130px;
  }
  .features-frame { position: absolute; inset: 0; }
  .feature {
    position: absolute; top: 8px; width: 220px; text-align: center;
    color: var(--navy); font-weight: 500; font-size: 20px; line-height: 1.15;
  }
  .feature svg { display: block; margin: 0 auto 6px; }
  .feature-units { left: 20px; }
  .feature-temp { left: 250px; }
  .feature-parking { left: 480px; }
  .address {
    position: absolute; left: 28px; top: 572px;
    display: flex; align-items: center; gap: 12px;
    color: var(--navy); font-weight: 900; font-size: 47px; letter-spacing: 0.5px;
    white-space: nowrap;
  }
  .device-showcase {
    position: absolute; left: 830px; top: 120px; width: 330px; height: 520px;
    border-radius: 22px;
    background: linear-gradient(160deg, #1d1c3f 0%, #3a3a6e 45%, #e9e9ee 46%, #ffffff 100%);
    border: 8px solid #2a2a30;
  }
  .contact-band { position: absolute; left: 0; top: 672px; width: 1200px; height: 113px; }
  .contact {
    position: absolute; top: 672px; height: 113px;
    display: flex; align-items: center; gap: 12px;
    color: var(--white); white-space: nowrap; line-height: 1;
  }
  .contact-web { left: 24px; font-weight: 500; font-size: 46px; }
  .contact-phone { left: 808px; font-weight: 600; font-size: 46px; letter-spacing: 0.5px; }
</style>
</head>
<body>
<main class="billboard">
  <svg class="backdrop" width="1200" height="785" viewBox="0 0 1200 785" aria-hidden="true">
    <polygon points="760,0 1200,0 1200,672 1010,672" fill="var(--navy)"/>
    <polygon points="690,0 760,0 1010,672 940,672" fill="var(--gold)"/>
    <polygon points="820,0 1200,0 1200,470" fill="#33327f" opacity="0.6"/>
  </svg>

  <div class="brand">
    <div class="brand-name">SAM GREENFIELD</div>
    <div class="brand-sub">SELF STORAGE</div>
  </div>

  <h1 class="headline">
    <div class="headline-top">RENT ONLINE</div>
    <div class="headline-bottom">ANYTIME!</div>
  </h1>

  <section class="features">
    <svg class="features-frame" width="720" height="130" viewBox="0 0 720 130" aria-hidden="true">
      <polyline points="30,128 2,128 2,28 718,28" fill="none" stroke="var(--navy)" stroke-width="3"/>
      <polyline points="718,28 718,118 690,118" fill="none" stroke="var(--navy)" stroke-width="3"/>
    </svg>
    <div class="feature feature-units">
      <svg width="60" height="46" viewBox="0 0 60 46" aria-hidden="true">
        <polygon points="4,18 30,4 56,18 56,44 4,44" fill="var(--gold)"/>
        <rect x="12" y="24" width="36" height="4" fill="var(--white)"/>
        <rect x="12" y="31" width="36" height="4" fill="var(--white)"/>
        <rect x="12" y="38" width="36" height="4" fill="var(--white)"/>
      </svg>
      Large/Small<br>Units
    </div>
    <div class="feature feature-temp">
      <svg width="60" height="46" viewBox="0 0 60 46" aria-hidden="true">
        <rect x="34" y="3" width="10" height="30" rx="5" fill="none" stroke="var(--gold)" stroke-width="3"/>
        <circle cx="39" cy="37" r="7" fill="var(--gold)"/>
        <rect x="37.5" y="16" width="3" height="18" fill="var(--gold)"/>
        <g stroke="var(--gold)" stroke-width="3" stroke-linecap="round">
          <line x1="18" y1="6" x2="18" y2="28"/>
          <line x1="8" y1="11" x2="28" y2="23"/>
          <line x1="8" y1="23" x2="28" y2="11"/>
        </g>
      </svg>
      Temperature<br>Controlled
    </div>
    <div class="feature feature-parking">
      <svg width="70" height="46" viewBox="0 0 70 46" aria-hidden="true">
        <rect x="6" y="4" width="58" height="30" rx="10" fill="var(--gold)"/>
        <rect x="16" y="11" width="14" height="10" fill="var(--white)"/>
        <circle cx="28" cy="38" r="6" fill="var(--white)" stroke="var(--gold)" stroke-width="3"/>
        <rect x="2" y="30" width="8" height="3" fill="var(--gold)"/>
      </svg>
      Coverd Boat/<br>RV Parking
    </div>
  </section>

  <div class="address">
    <svg width="56" height="60" viewBox="0 0 56 60" aria-hidden="true">
      <polygon points="0,30 54,0 40,30 54,60" fill="var(--navy)"/>
    </svg>
    418 MAPLE RIDGE DRIVE
  </div>

  <div class="device-showcase" role="img" aria-label="Tablet and phone showing the online unit rental website"></div>

  <svg class="contact-band" width="1200" height="113" viewBox="0 0 1200 113" aria-hidden="true">
    <polygon points="0,0 800,0 770,113 0,113" fill="var(--gold)"/>
    <polygon points="812,0 1200,0 1200,113 782,113" fill="var(--navy)"/>
  </svg>

  <div class="contact contact-web">
    <svg width="38" height="38" viewBox="0 0 40 40" aria-hidden="true">
      <circle cx="20" cy="20" r="17" fill="none" stroke="var(--navy)" stroke-width="3"/>
      <ellipse cx="20" cy="20" rx="7" ry="17" fill="none" stroke="var(--navy)" stroke-width="2.5"/>
      <line x1="3" y1="20" x2="37" y2="20" stroke="var(--navy)" stroke-width="2.5"/>
    </svg>
    SamGreenfieldStorage.com
  </div>

  <div class="contact contact-phone">
    <svg width="36" height="36" viewBox="0 0 24 24" aria-hidden="true">
      <path d="M6.6 10.8a15.1 15.1 0 0 0 6.6 6.6l2.2-2.2a1 1 0 0 1 1-.25 11.4 11.4 0 0 0 3.6.57 1 1 0 0 1 1 1V20a1 1 0 0 1-1 1A17 17 0 0 1 3 4a1 1 0 0 1 1-1h3.5a1 1 0 0 1 1 1c0 1.25.2 2.45.57 3.57a1 1 0 0 1-.25 1z" fill="var(--gold)"/>
    </svg>
    555-014-2738
  </div>
</main>
</body>
</html>
```